Guaranteed Web Design (Uncoded - PSD layout only) for kids psychologists, minor logo with runner up

Simple psychologist website
Open brief, creative designs encouraged
Site map:
Home
our services
our psychologists
selective mutism
resources
contact

Current website:
http://mindnest4tots.com.au/
Not in love with our logo, or colours etc - open brief
Happy for new font/style/logo for company name - if we choose a logo design from a designer who doesn't win the competition, we will award $50 for the logo and use it in the new website

Website made a few years ago for a sister company that we really like:
http://www.corlewpsychology.com.au/

Clean, credible and warm and friendly look & feel
stock photos OK, designer will be required to hand over any images used in the design as shown in the PSD

Target Market(s)

Adolescents with psychological issues and their families

Industry/Entity Type

Psychology

Number of Pages Required

2 page

Colors

Designer to choose colors to be used in the design.

Requirements
Must have
• One home page - simple with 2 or 3 small areas to tease and attract the user and one template page to suit all the other pages
• We like slides, we want to have 3 slides like corlewpsychology.com.au
• Three slide titles:
• 1. We specialise in many areas, find the right clinical psychologist for your family
• 2. Child Clinical Psychologists in Ashbourne and Kelmdale
• 3. Resources
• Pages structurally similar to
• http://www.corlewpsychology.com.au/
• We like the 'featured' items, which in our case will have splash box titles (can be 3 or 4):
• 1. Selective Mutism
• 2. Is my child anxious?
• 3. Does my child have an eating disorder?
• 4. Parenting adolescents
• Does not need to be a copy of http://www.corlewpsychology.com.au/ and we are willing to accept outside-the-box thinking and design (we in fact encourage it)
• Owner of business wants to highlight Selective Mutism as they have specialists. Consider ways that may make this work.
• Design winner will be based on home page design but winning designer will be required to provide an additional but simpler 'standard' page template design based on the themes used in the winning design.

```html
<!DOCTYPE html>
<html lang="en">
<head>
<meta charset="utf-8">
<title>MindNest – Child, Adolescent &amp; Family Psychology</title>
<link rel="stylesheet" href="https://fonts.googleapis.com/css2?family=Montserrat:wght@400;500;600&family=Raleway:wght@400;500&display=swap">
<style>
  :root {
    --hero-deep: #3f3f86;
    --hero-mid: #56559e;
    --hero-warm: #6e5a8e;
    --white: #ffffff;
    --nav-muted: rgba(255, 255, 255, 0.62);
    --nav-rule: rgba(255, 255, 255, 0.7);
  }
  * { box-sizing: border-box; margin: 0; padding: 0; }
  html, body { width: 1200px; height: 667px; overflow: hidden; }
  body { font-family: "Montserrat", Arial, sans-serif; color: var(--white); }

  .hero { position: relative; width: 1200px; height: 667px; overflow: hidden; }

  .hero-photo {
    position: absolute; inset: 0;
    background:
      radial-gradient(ellipse 260px 220px at 700px 400px, rgba(150, 170, 130, 0.35), transparent 70%),
      radial-gradient(ellipse 300px 380px at 880px 330px, rgba(40, 40, 100, 0.55), transparent 75%),
      radial-gradient(ellipse 200px 160px at 560px 520px, rgba(160, 120, 150, 0.3), transparent 70%),
      linear-gradient(180deg, var(--hero-mid) 0%, var(--hero-deep) 45%, var(--hero-warm) 75%, var(--hero-deep) 100%);
  }

  .brand { position: absolute; left: 42px; top: 38px; }
  .brand-name {
    display: flex; align-items: center; gap: 9px;
    font-weight: 600; font-size: 31px; letter-spacing: 1.5px; line-height: 1;
  }
  .brand-dot { width: 30px; height: 30px; border: 2px solid var(--white); border-radius: 50%; }
  .brand-tagline { margin-top: 10px; font-size: 11.5px; letter-spacing: 0.8px; font-weight: 400; }

  .main-nav { position: absolute; left: 419px; top: 0; right: 0; height: 95px; border-bottom: 1px solid var(--nav-rule); }
  .main-nav a {
    position: absolute; top: 38px; font-size: 15px; font-weight: 500;
    color: var(--nav-muted); text-decoration: none; white-space: nowrap;
  }
  .main-nav a.is-active { color: var(--white); }
  .main-nav a.is-active::after {
    content: ""; position: absolute; left: 0; right: 0; top: 54px; height: 4px; background: var(--white);
  }

  .slide-copy { position: absolute; left: 217px; top: 134px; font-family: "Raleway", Arial, sans-serif; }
  .slide-kicker { font-size: 20px; font-weight: 500; }
  .slide-title { margin-top: 22px; font-size: 52px; font-weight: 400; line-height: 67px; }
  .slide-rule { margin-top: 28px; width: 45px; height: 3px; background: var(--white); }

  .slide-dots { position: absolute; left: 217px; top: 605px; display: flex; gap: 42px; }
  .slide-dot { width: 20px; height: 20px; border: 2px solid var(--white); border-radius: 50%; }
  .slide-dot.is-current { background: var(--white); }
</style>
</head>
<body>
<header class="hero">
  <div class="hero-photo" role="img" aria-label="Parent walking hand in hand with a small child carrying a teddy bear along a forest path, tinted violet"></div>

  <div class="brand">
    <div class="brand-name"><span class="brand-dot"></span>MindNest</div>
    <div class="brand-tagline">Child, Adolescent &amp; Family Psychology</div>
  </div>

  <nav class="main-nav">
    <a class="is-active" href="#" style="left:0">Home</a>
    <a href="#" style="left:85px">About Us</a>
    <a href="#" style="left:196px">For Parents</a>
    <a href="#" style="left:320px">For Professionals</a>
    <a href="#" style="left:485px">For Teens</a>
    <a href="#" style="left:595px">Blog</a>
    <a href="#" style="left:668px">Contact Us</a>
  </nav>

  <section class="slide-copy">
    <p class="slide-kicker">Child Clinical Psychologists in</p>
    <h1 class="slide-title">Ashbourne<br>and Kelmdale</h1>
    <div class="slide-rule"></div>
  </section>

  <div class="slide-dots">
    <span class="slide-dot"></span>
    <span class="slide-dot is-current"></span>
    <span class="slide-dot"></span>
  </div>
</header>
</body>
</html>
```